Hair and Wellness Brochure and Pricelist design

I am requiring a brochure that has a fresh, though alternative design. My business name is The Quiet Harbor Hair and Wellness. I have a very professional approach to my work and love to give that little bit extra to all of my clients. My passion for health, has led me to channel my business alternatively by using non toxic colours and styling products and through that same vein, I have studied Aromatherapy, Indian Head Massage and Reiki...all additional services I use where required.
My studio has very neutral tones of beige,white and beech wood but these tones aren't necessarily required for the brochure.I like to create a space of calm, peace and quiet, where my clients feel refreshed and rejuvenated..

```html
<!DOCTYPE html>
<html lang="en">
<head>
<meta charset="utf-8">
<title>The Quiet Harbor Hair and Wellness – Brochure and Pricelist</title>
<link href="https://fonts.googleapis.com/css2?family=Ubuntu:wght@400;500&display=swap" rel="stylesheet">
<style>
  :root {
    --stage: #e9e6e1;
    --cocoa: #6e4d40;
    --wave-light: #c7b6a7;
    --wave-mid: #a88f80;
    --wave-deep: #8b6f61;
    --cream: #f8f5e3;
    --tile: #7a6258;
    --tile-text: #fbf7ee;
    --ink-soft: #8a7468;
    --ornament: #c9b7a8;
  }
  * { box-sizing: border-box; margin: 0; padding: 0; }
  html, body { width: 1200px; height: 960px; overflow: hidden; }
  body {
    background: var(--stage);
    font-family: "Ubuntu", sans-serif;
    position: relative;
  }
  .panel {
    position: absolute;
    overflow: hidden;
    box-shadow: 0 2px 6px rgba(0,0,0,.25);
  }
  .panel svg.waves { position: absolute; left: 0; top: 0; }

  /* Cover */
  .cover { left: 62px; top: 30px; width: 565px; height: 439px; background: var(--cocoa); }
  .cover .brand {
    position: absolute; left: 388px; top: 176px; width: 170px;
    color: var(--cream); font-weight: 500; font-size: 17px; line-height: 1.15;
  }
  .cover .brand small { display: block; font-size: 9px; font-weight: 500; letter-spacing: .5px; margin-top: 3px; }
  .cover .tagline {
    position: absolute; left: 389px; top: 246px;
    color: #f3ece2; font-size: 8.5px;
  }
  .cover .ornament {
    position: absolute; left: 421px; top: 312px; width: 144px; height: 120px;
    background: radial-gradient(ellipse at 70% 60%, rgba(201,183,168,.55), rgba(201,183,168,0) 70%);
  }
  .cover .footer-name {
    position: absolute; left: 250px; top: 414px;
    color: var(--wave-light); font-size: 8px; font-weight: 500;
  }

  /* Pricelist */
  .pricelist { left: 600px; top: 491px; width: 567px; height: 442px; background: var(--cream); }
  .pricelist .ornament {
    position: absolute; left: 0; top: 0; width: 150px; height: 120px;
    background: radial-gradient(ellipse at 25% 30%, rgba(138,116,104,.5), rgba(138,116,104,0) 70%);
  }
  .price {
    position: absolute; width: 146px;
    display: flex; flex-direction: column; justify-content: center; align-items: center;
    background: var(--tile); color: var(--tile-text);
    font-size: 8.5px; line-height: 1.25; text-align: center;
    border-radius: 3px; padding: 3px 6px;
    box-shadow: 1px 2px 3px rgba(0,0,0,.3);
  }
  .col-a { left: 26px; }
  .col-b { left: 211px; }
  .col-c { left: 399px; }
  .note {
    position: absolute; left: 204px; top: 283px;
    font-size: 6px; color: var(--ink-soft);
  }
  .pricelist .footer-name {
    position: absolute; right: 30px; top: 410px; text-align: right;
    color: var(--cream); font-size: 15px; font-weight: 500; line-height: 1.1;
  }
  .pricelist .footer-name small { display: block; font-size: 7px; letter-spacing: 1px; }
</style>
</head>
<body>

<section class="panel cover">
  <svg class="waves" width="565" height="439" viewBox="0 0 565 439" aria-hidden="true">
    <path fill="var(--wave-deep)" d="M0,0 H565 V55 C470,60 400,120 300,140 C200,160 90,150 0,135 Z"/>
    <path fill="var(--wave-mid)" d="M0,0 H565 V35 C470,38 390,90 290,105 C190,120 90,110 0,95 Z"/>
    <path fill="var(--wave-light)" d="M0,0 H565 V15 C470,15 400,55 300,68 C200,80 100,70 0,58 Z"/>
  </svg>
  <div class="brand">The Quiet Harbor<small>Hair and Wellness</small></div>
  <p class="tagline">Aromatherapy, Indian Head Massage and Reiki</p>
  <div class="ornament" role="img" aria-label="Flowing floral swirl ornament"></div>
  <p class="footer-name">The Quiet Harbor</p>
</section>

<section class="panel pricelist">
  <svg class="waves" width="567" height="442" viewBox="0 0 567 442" aria-hidden="true">
    <path fill="var(--wave-light)" d="M0,395 C120,400 240,360 330,320 C420,285 500,285 567,290 V442 H0 Z"/>
    <path fill="var(--wave-mid)" d="M0,410 C130,410 250,380 340,345 C430,312 510,310 567,318 V442 H0 Z"/>
    <path fill="var(--wave-deep)" d="M0,425 C140,422 260,395 350,368 C440,342 510,340 567,345 V442 H0 Z"/>
  </svg>
  <div class="ornament" role="img" aria-label="Flowing floral swirl ornament"></div>

  <div class="price col-a" style="top:158px;height:38px">Shampoo &amp; blow dry<br>$40</div>
  <div class="price col-a" style="top:212px;height:47px">Hot tool styling with Shampoo included<br>$50</div>
  <div class="price col-a" style="top:273px;height:39px">Shampoo cut &amp; blow dry<br>$70</div>
  <div class="price col-a" style="top:330px;height:38px">Men's style cut<br>$30</div>

  <div class="price col-b" style="top:26px;height:47px">Tint &amp; semi permanent regrowth colour<br>$60</div>
  <div class="price col-b" style="top:91px;height:38px">Half head foiling techniques<br>$60</div>
  <div class="price col-b" style="top:151px;height:38px">Full head foiling techniques<br>$120</div>
  <div class="price col-b" style="top:208px;height:48px">Any additional colour with the above colour services starts from<br>$20</div>
  <p class="note">* Corrective colour services are priced at consultation</p>

  <div class="price col-c" style="top:26px;height:57px">Indian Head Massage with a Reiki and Aromatherapy Infusion<br>45mins<br>$50</div>
  <div class="price col-c" style="top:99px;height:39px">Hair up styling including hot tools<br>$50</div>
  <div class="price col-c" style="top:154px;height:49px">All wedding hairstyling starts from<br>$60 (Price on consultation)</div>
  <div class="price col-c" style="top:220px;height:38px">Wedding up style consultation<br>$50</div>

  <div class="footer-name">The Quiet Harbor<small>Hair and Wellness</small></div>
</section>

</body>
</html>
```